Needs Vehicle wrap ideas. Creating a branding look for future marketing

I have a logo and need a vehicle wrap design made. The concept that is on the wrap with be applied in a similar way to all future marketing material for our company. For example once we get the wrap design made, anytime we create a postcard or flyer or business card, we'll use the same branding look. The vehicle I would like to get the design made on is a Marlow Cargo 250 midroof. We are open to all ideas but would love to find a designer that can work off our logo and business category to come up with a great branding look. (we currently use the top right logo in the attached file)phone number is 555-214-WARM our website is BRISKCLIMATEPROS.EXAMPLE we offer service, installation and maintenance

Target Market(s)

Heating and Cooling

Industry/Entity Type

Heating

Colors
3176b5
85acd3
0455a3
7f7f7f
5c5c5c

Requirements
Must have
• Original design, no pre-made templates. Design must have the logo (top right on attached file), phone number, website, and should list Service, Installation, and Maintenance
Should not have
• No images of people.

```html
<!DOCTYPE html>
<html lang="en">
<head>
<meta charset="utf-8">
<title>Brisk Climate Pros – Vehicle Wrap</title>
<link rel="stylesheet" href="https://fonts.googleapis.com/css2?family=Montserrat:wght@600;700;900&family=Roboto+Condensed:wght@500&display=swap">
<style>
  :root{
    --blue:#0455a3;
    --blue-mid:#3176b5;
    --blue-light:#85acd3;
    --navy:#1c2a86;
    --grey:#7f7f7f;
    --grey-dark:#5c5c5c;
    --white:#ffffff;
    --page:#f3f5f7;
    --accent-red:#c4262e;
  }
  html,body{margin:0;padding:0;overflow:hidden;background:var(--page);}
  .canvas{width:1200px;height:857px;display:block;}
  .brand{font-family:"Montserrat",sans-serif;font-weight:900;fill:var(--navy);}
  .sub{font-family:"Montserrat",sans-serif;font-weight:700;letter-spacing:3px;}
  .label{font-family:"Montserrat",sans-serif;font-weight:700;}
  .web{font-family:"Montserrat",sans-serif;font-weight:600;}
  .emergency{font-family:"Roboto Condensed",sans-serif;font-weight:500;fill:var(--white);}
</style>
</head>
<body>
<svg class="canvas" viewBox="0 0 1200 857" xmlns="http://www.w3.org/2000/svg">

  <!-- Side panel -->
  <g class="side-panel" transform="translate(150,60)">
    <clipPath id="side-clip"><rect width="900" height="290" rx="18"/></clipPath>
    <g clip-path="url(#side-clip)">
      <rect class="base" width="900" height="290" fill="var(--white)"/>
      <polygon class="band-grey" points="0,300 900,109 900,290 0,290" fill="var(--grey)"/>
      <polygon class="band-blue-low" points="470,290 900,199 900,290" fill="var(--blue)"/>
      <polygon class="band-grey-cab" points="55,290 75,195 210,195 300,290" fill="var(--grey)"/>
      <polygon class="fender-blue" points="0,160 75,195 55,290 0,290" fill="var(--blue)"/>
      <polygon class="band-blue-top" points="0,0 823,0 0,175" fill="var(--blue)"/>
    </g>

    <g class="diagonal" transform="rotate(-12)">
      <text class="label" x="190" y="110" font-size="24" fill="var(--white)">CALL US:</text>
      <text class="label" x="150" y="150" font-size="32" fill="var(--white)">555-214-WARM</text>
      <text class="brand" x="300" y="262" font-size="100">BRISK</text>
      <text class="sub" x="670" y="290" font-size="22" text-anchor="end" fill="var(--grey-dark)">CLIMATE PROS</text>
      <text class="label" x="680" y="318" font-size="14" text-anchor="end" fill="var(--white)" letter-spacing="0.5">DEPENDABLE, PROFESSIONAL AND HONEST</text>
      <text class="web" x="680" y="340" font-size="13" text-anchor="end" fill="var(--white)" letter-spacing="0.5">BRISKCLIMATEPROS.EXAMPLE</text>
      <g class="social" fill="none" stroke="var(--white)" stroke-width="1.6">
        <circle cx="720" cy="322" r="10"/>
        <circle cx="746" cy="322" r="10"/>
      </g>
    </g>

    <g class="services" transform="translate(745,40) rotate(-12)" fill="var(--blue)">
      <text class="label" font-size="14"><tspan x="0" y="0">✓ SERVICE</tspan><tspan x="4" y="18">✓ INSTALLATION</tspan><tspan x="8" y="36">✓ MAINTENANCE</tspan></text>
    </g>

    <rect class="badge" x="842" y="215" width="26" height="40" rx="3" fill="none" stroke="var(--white)" stroke-width="2"/>

    <g class="support" transform="translate(165,228)">
      <circle cx="-14" cy="0" r="13" fill="none" stroke="var(--white)" stroke-width="3"/>
      <path d="M-14,-7 V0 L-8,4" fill="none" stroke="var(--white)" stroke-width="2.5"/>
      <text class="emergency" x="4" y="7" font-size="19">24h/7</text>
      <text class="emergency" x="0" y="34" font-size="16" text-anchor="middle">Emergency Support</text>
    </g>
  </g>

  <!-- Rear panel -->
  <g class="rear-panel" transform="translate(430,430)">
    <clipPath id="rear-clip"><rect width="340" height="390" rx="20"/></clipPath>
    <g clip-path="url(#rear-clip)">
      <rect width="340" height="390" fill="var(--white)"/>
      <polygon class="top-band" points="0,0 340,0 315,40 25,40" fill="var(--blue)"/>
      <rect class="low-grey" x="0" y="250" width="340" height="140" fill="var(--grey)"/>
      <polygon class="low-blue" points="0,250 340,250 340,330 150,330 110,280 0,280" fill="var(--blue)"/>
      <rect class="bumper" x="0" y="330" width="340" height="60" fill="var(--grey-dark)"/>
    </g>
    <line x1="170" y1="0" x2="170" y2="330" stroke="var(--grey)" stroke-width="1" opacity=".5"/>
    <text class="brand" x="170" y="118" font-size="66" text-anchor="middle">BRISK</text>
    <line x1="60" y1="130" x2="280" y2="130" stroke="var(--accent-red)" stroke-width="2"/>
    <text class="sub" x="170" y="156" font-size="19" text-anchor="middle" fill="var(--grey-dark)">CLIMATE PROS</text>
    <text class="label" x="170" y="196" font-size="26" text-anchor="middle" fill="var(--blue)">CALL US:</text>
    <text class="label" x="170" y="226" font-size="28" text-anchor="middle" fill="var(--blue)">555-214-WARM</text>
    <text class="web" x="320" y="280" font-size="11" text-anchor="end" fill="var(--white)">BRISKCLIMATEPROS.EXAMPLE</text>
    <g fill="none" stroke="var(--white)" stroke-width="1.4">
      <circle cx="290" cy="300" r="9"/>
      <circle cx="314" cy="300" r="9"/>
    </g>
    <rect class="badge" x="30" y="280" width="24" height="36" rx="3" fill="none" stroke="var(--white)" stroke-width="2"/>
  </g>
</svg>
</body>
</html>
```